needing web design for aerial and satellite installation comapny

We need our website designing, it needs to be professional and look creative,
We are a aerial and satellite company called Brindle Fixing & Tending ()
I like this site design also some of the following maybe:

https://www.corvimast.co.uk/

http://quellmoor.co.uk/

http://larkpin4guard.co.uk/portfolio/tdn-quellmoor/

The design will require coding once the design is complete, i haven't paid for this yet as i want to be sure the design is good before i commit.

The template needs to look professional and look like one of the leading companies.
The site will consist of all the features this site has https://www.corvimast.co.uk/

I like a modern design with the latest technology.

Target Market(s)

tv aerial satellite installation

Industry/Entity Type

Satellite Tv

Number of Pages Required

3 page

Font styles to use
Sans Serif

Colors

Designer to choose colors to be used in the design.

Requirements
Must have
• eb Contest Brief We need our website designing, it needs to be professional and look creative,
• We are a aerial and satellite company called Brindle Fixing Tending ()
• I like this site design also some of the following maybe:
• https://www.corvimast.co.uk/
• http://quellmoor.co.uk/
• http://larkpin4guard.co.uk/portfolio/tdn-quellmoor/
• The design will require coding once the design is complete, i haven't paid for this yet as i want to be sure the design is good before i commit.
• The template needs to look professional and look like one of the leading companies.
• The site will consist of all the features this site has https://www.corvimast.co.uk/
• I like a modern design with the latest technology.
Nice to have
• http://quellmoor.co.uk/
Should not have
• poor design

```html
<!DOCTYPE html>
<html lang="en">
<head>
<meta charset="utf-8">
<title>Brindle Fixing &amp; Tending — Aerial and Satellite Installation</title>
<link href="https://fonts.googleapis.com/css2?family=Open+Sans:wght@400;600;700;800&display=swap" rel="stylesheet">
<style>
:root{
  --ink:#222;
  --text:#555;
  --dark:#2b2b2b;
  --card:#464646;
  --card-foot:#353535;
  --light:#ececec;
  --band:#e8e8e8;
  --footer:#2a2a2a;
  --footer-base:#1c1c1c;
  --muted:#8a8a8a;
  --white:#fff;
}
*{box-sizing:border-box;margin:0;padding:0}
html,body{width:1200px;height:2975px;overflow:hidden}
body{font-family:'Open Sans',Arial,sans-serif;color:var(--text);background:var(--white);position:relative}
.wrap{position:absolute;left:133px;width:934px}
a{color:inherit;text-decoration:none}

/* header */
.utility{position:absolute;left:440px;top:0;width:760px;height:48px;background:var(--dark);
  clip-path:polygon(0 0,100% 0,100% 100%,24px 100%);display:flex;align-items:center;gap:38px;padding-left:58px;font-size:13px;color:#ccc}
.utility span{display:flex;align-items:center;gap:8px}
.utility svg{width:13px;height:13px;fill:#bbb}
.brand{position:absolute;left:133px;top:18px;width:290px}
.brand-mark{display:block;margin-left:96px;width:66px;height:66px;background:var(--ink)}
.brand-name{margin-top:26px;font-size:15px;font-weight:700;letter-spacing:8px;color:var(--ink)}
.brand-sub{margin-top:4px;font-size:13px;letter-spacing:9px;color:var(--ink);padding-left:104px}
.nav{position:absolute;right:133px;top:117px;display:flex;gap:28px;font-size:13px;color:var(--ink)}
.nav .active{border-bottom:1px solid var(--ink)}

/* hero */
.hero{position:absolute;left:0;top:180px;width:1200px;height:435px;overflow:hidden}
.hero-photo{position:absolute;inset:0;background:linear-gradient(180deg,#4a5b7a 0%,#9a7a6a 38%,#e39a3a 62%,#f2b03a 78%,#6b4a2a 100%)}
.hero-panel{position:absolute;left:0;top:0;width:560px;height:435px;background:#242424;clip-path:polygon(0 0,540px 0,400px 435px,0 435px)}
.hero-copy{position:absolute;left:131px;top:100px;width:300px}
.hero-copy h1{font-size:34px;line-height:40px;font-weight:700;color:#bdbdbd}
.hero-copy p{margin-top:12px;font-size:12px;line-height:18px;color:#9a9a9a}
.btn-light{display:inline-block;margin-top:18px;background:#bdbdbd;color:var(--ink);font-size:14px;font-weight:700;padding:10px 14px}
.hero-next{position:absolute;right:30px;top:203px;width:28px;height:28px;border-radius:50%;background:#333;display:flex;align-items:center;justify-content:center}

/* intro */
.section-title{font-size:32px;font-weight:700;color:var(--ink);text-align:center;text-transform:uppercase}
.intro{top:686px}
.intro p{margin-top:16px;font-size:12.5px;line-height:21px;text-align:center}
.services{top:865px;display:flex;gap:22px}
.service{width:218px;height:257px;background:var(--card);color:var(--white);text-align:center;position:relative}
.service svg{margin-top:28px;width:62px;height:62px;stroke:#fff;fill:none;stroke-width:2.2;stroke-linecap:round;stroke-linejoin:round}
.service h3{margin-top:14px;font-size:19px;font-weight:700;text-transform:uppercase}
.service p{margin:8px 20px 0;font-size:10px;line-height:15px;color:#d2d2d2}
.service .more{position:absolute;left:0;bottom:0;width:100%;height:40px;line-height:40px;background:var(--card-foot);font-size:11px}

/* process band */
.process{position:absolute;left:0;top:1202px;width:1200px;height:448px;background:radial-gradient(ellipse at 50% 45%,#5b6a4c 0%,#3a3a34 45%,#252422 100%)}
.process h2{position:absolute;top:72px;width:100%;text-align:center;font-size:31px;font-weight:700;color:var(--white);text-transform:uppercase}
.step{position:absolute;top:142px;width:260px;text-align:center;color:var(--white)}
.step .ring{margin:0 auto;width:160px;height:160px;border:1px solid rgba(255,255,255,.8);border-radius:50%;display:flex;align-items:center;justify-content:center}
.step svg{width:46px;height:46px}
.step p{margin-top:18px;font-size:16px;line-height:24px}
.connector{position:absolute;top:222px;height:1px;width:148px;background:rgba(255,255,255,.8)}

/* feature boxes */
.features{top:1723px;display:flex;gap:24px}
.feature{width:295px;height:240px;background:var(--light);text-align:center;padding-top:18px}
.feature svg{width:28px;height:28px;fill:var(--ink)}
.feature h3{font-size:32px;font-weight:700;color:var(--ink);line-height:40px}
.feature p{margin:10px 36px 0;font-size:10px;line-height:15px}
.feature .field{margin:22px auto 0;width:242px;height:40px;border:1px solid #ccc;background:var(--white);text-align:left;padding:12px 12px;font-size:10px;color:#999}
.btn-dark{display:inline-block;margin-top:18px;background:#3a3a3a;color:var(--white);font-size:12px;font-weight:700;padding:11px 19px}

/* testimonials */
.testimonials{position:absolute;left:0;top:2043px;width:1200px;height:337px;background:var(--band)}
.testimonials h2{margin-top:72px}
.quote{margin:10px auto 0;width:934px;font-size:16px;line-height:28px;text-align:center;color:#444}
.quote b{font-size:18px;color:var(--ink)}
.cite{margin-top:6px;text-align:center;font-size:16px;color:#444}
.dots{margin-top:12px;display:flex;justify-content:center;gap:14px}
.dots i{width:9px;height:9px;border-radius:50%;background:#ccc}
.dots i:first-child{background:var(--ink)}

/* partners */
.partners{top:2466px;display:flex;justify-content:space-between;align-items:center;font-size:18px;font-weight:700;color:#333}

/* footer */
.footer{position:absolute;left:0;top:2582px;width:1200px;height:343px;background:var(--footer);color:var(--muted)}
.footer .tagline{position:absolute;left:133px;top:44px;width:934px;text-align:center;font-size:18px;color:#8f8f8f;text-transform:uppercase;padding-bottom:20px;border-bottom:1px solid #555}
.cols{position:absolute;left:133px;top:142px;width:934px;display:flex}
.col{width:168px}
.col h4{font-size:14px;color:var(--white);font-weight:700;margin-bottom:10px}
.col li{list-style:none;font-size:10.5px;line-height:23px}
.col li::before{content:"› ";}
.col.wide{width:262px}
.col.wide h4{font-size:15px;line-height:22px}
.col.wide p{margin-top:10px;font-size:10px;line-height:16px}
.social{margin-top:22px;display:flex;gap:14px}
.social i{width:28px;height:28px;border:1px solid #777;border-radius:50%}
.base{position:absolute;left:0;top:2925px;width:1200px;height:50px;background:var(--footer-base);color:#888;font-size:10.5px;text-align:center;line-height:50px}
</style>
</head>
<body>

<header>
  <div class="utility">
    <span><svg viewBox="0 0 16 16"><circle cx="8" cy="5" r="3.5"/><path d="M1 16c0-4 3-6 7-6s7 2 7 6z"/></svg>My Account</span>
    <span><svg viewBox="0 0 16 16"><path d="M1 7h9L7 4l1-1 5 5-5 5-1-1 3-3H1zM11 1h4v14h-4v-1.5h2.5v-11H11z"/></svg>Login</span>
    <span><svg viewBox="0 0 16 16"><path d="M1 3h8v1.5H2.5v9h9V9H13v6H1zM12 1l3 3-7 7H5V8z"/></svg>Register</span>
    <span><svg viewBox="0 0 16 16"><rect x="4" y="0" width="8" height="16" rx="1.5"/></svg>654 555 0192</span>
    <span><svg viewBox="0 0 16 16"><path d="M0 1h3l1 2h12l-2 7H5l-1 2h11v1.5H2l2-4L2 2.5H0z"/><circle cx="5" cy="15" r="1"/><circle cx="13" cy="15" r="1"/></svg>Cart - 0</span>
  </div>
  <div class="brand">
    <span class="brand-mark" aria-hidden="true"></span>
    <div class="brand-name">BRINDLE FIXING</div>
    <div class="brand-sub">&amp; TENDING</div>
  </div>
  <nav class="nav">
    <a class="active">Home</a><a>Services</a><a>Products</a><a>Support</a><a>Contact Us</a>
  </nav>
</header>

<section class="hero">
  <div class="hero-photo" role="img" aria-label="Satellite dishes silhouetted against an orange sunset sky"></div>
  <div class="hero-panel"></div>
  <div class="hero-copy">
    <h1>AERIAL AND SATELLITE INSTALLATION</h1>
    <p>Duis ornare erat eget magna dapibus, in accumsan quam pharetra. Nam tempus, quam in.</p>
    <a class="btn-light">CONTACT US</a>
  </div>
  <div class="hero-next"><svg width="12" height="12" viewBox="0 0 12 12"><path d="M4 1l5 5-5 5" stroke="#fff" stroke-width="2.4" fill="none"/></svg></div>
</section>

<section class="wrap intro">
  <h2 class="section-title">Pellentesque Blandit</h2>
  <p>Phasellus consequat sagittis nisi suscipit feugiat. Cras eget leo sed nunc hendrerit ultricies eu at nisl. Praesent iaculis faucibus urna sit amet lacinia. Maecenas consequat justo enim, ac mattis massa imperdiet quis. Fusce eget neque elit. Sed augue orci, elementum in magna congue, tincidunt vulputate erat. Aliquam consectetur orci molestie dictum molestie. Proin eget congue nulla, vel tempor diam. Ut non ante est. Fusce sollicitudin lorem et luctus volutpat. Proin placerat dapibus gravida. In tristique tristique nulla eget hendrerit. Maecenas vel tortor accumsan quam varius imperdiet vel eget</p>
</section>

<section class="wrap services">
  <article class="service">
    <svg viewBox="0 0 64 64"><path d="M14 22a26 26 0 0 0 28 28z"/><path d="M28 36l14-14M42 22l-2-2"/><path d="M22 46l-6 12h20l-6-10"/><path d="M46 12a10 10 0 0 1 6 6M48 6a16 16 0 0 1 10 10"/></svg>
    <h3>Aenean Facilisis</h3>
    <p>Quisque aliquet ex nec est vestibu lum pulvinar. Pellentesque convallis molestie enim sit amet efficitur.</p>
    <div class="more">READ MORE</div>
  </article>
  <article class="service">
    <svg viewBox="0 0 64 64"><circle cx="32" cy="24" r="5"/><path d="M22 14a14 14 0 0 0 0 20M42 14a14 14 0 0 1 0 20M16 8a22 22 0 0 0 0 32M48 8a22 22 0 0 1 0 32"/><path d="M32 29v31M24 60h16"/></svg>
    <h3>Fusce</h3>
    <p>Quisque aliquet ex nec est vestibu lum pulvinar. Pellentesque convallis molestie enim sit amet efficitur.</p>
    <div class="more">READ MORE</div>
  </article>
  <article class="service">
    <svg viewBox="0 0 64 64"><rect x="26" y="26" width="12" height="12" transform="rotate(45 32 32)"/><path d="M24 24L10 10M40 40l14 14"/><rect x="4" y="14" width="12" height="8" transform="rotate(-45 10 18)"/><rect x="48" y="42" width="12" height="8" transform="rotate(-45 54 46)"/><path d="M14 50a8 8 0 0 0 6 6M10 50a12 12 0 0 0 10 10"/></svg>
    <h3>Nulla Facilisi</h3>
    <p>Quisque aliquet ex nec est vestibu lum pulvinar. Pellentesque convallis molestie enim sit amet efficitur.</p>
    <div class="more">READ MORE</div>
  </article>
  <article class="service">
    <svg viewBox="0 0 64 64"><path d="M10 54l26-26M36 28a10 10 0 1 0 8-14l-6 6-4-4 6-6a10 10 0 0 0-12 12"/><path d="M54 54L30 30M8 8l6 2 8 8-4 4-8-8z"/><path d="M46 50l4-4 8 8-4 4z"/></svg>
    <h3>Etiam Vel</h3>
    <p>Quisque aliquet ex nec est vestibu lum pulvinar. Pellentesque convallis molestie enim sit amet efficitur.</p>
    <div class="more">READ MORE</div>
  </article>
</section>

<section class="process" role="img" aria-label="Blurred living room with a television and a hand holding a remote control">
  <h2>Vestibulum Condimentum</h2>
  <div class="step" style="left:142px">
    <div class="ring"><svg viewBox="0 0 48 48" fill="none" stroke="#fff" stroke-width="3.5"><path d="M26 8H8v32h32V22"/><path d="M20 28l2-8 16-16 6 6-16 16z" fill="#fff"/></svg></div>
    <p>Pellentesque convallis molestie enim sit amet efficitur.</p>
  </div>
  <div class="connector" style="left:352px"></div>
  <div class="step" style="left:469px">
    <div class="ring"><svg viewBox="0 0 48 48" fill="#fff"><circle cx="7" cy="10" r="4"/><circle cx="7" cy="24" r="4"/><circle cx="7" cy="38" r="4"/><rect x="15" y="7" width="30" height="6" rx="1"/><rect x="15" y="21" width="30" height="6" rx="1"/><rect x="15" y="35" width="30" height="6" rx="1"/></svg></div>
    <p>Aenean placerat, nibh vel accumsan aliquet, magna nibh</p>
  </div>
  <div class="connector" style="left:680px"></div>
  <div class="step" style="left:798px">
    <div class="ring"><svg viewBox="0 0 48 48" fill="#fff"><path d="M2 6h44v30H2zM6 10v22h36V10z"/><rect x="20" y="36" width="8" height="5"/><rect x="13" y="41" width="22" height="3"/></svg></div>
    <p>Cras augue magna, placerat eget nulla non, congue suscipi</p>
  </div>
</section>

<section class="wrap features">
  <article class="feature">
    <svg viewBox="0 0 28 28"><circle cx="14" cy="14" r="13"/><path d="M10 11a4 4 0 1 1 5.5 3.7c-1 .5-1.5 1-1.5 2.3" stroke="#ececec" stroke-width="2.6" fill="none"/><circle cx="14" cy="20.5" r="1.7" fill="#ececec"/></svg>
    <h3>FAQS</h3>
    <p>Phasellus nisl est, condimentum vitae faucibus in, sollicitudin vel metus. Nunc sit amet consequat risus. Curabitur ac elit leo.</p>
    <a class="btn-dark">READ MORE</a>
  </article>
  <article class="feature">
    <svg viewBox="0 0 28 28"><path d="M1 5h26v3L14 16 1 8z"/><path d="M1 11l13 8 13-8v12H1z"/></svg>
    <h3>NEWSLETTER</h3>
    <div class="field">Email Address</div>
    <a class="btn-dark">READ MORE</a>
  </article>
  <article class="feature">
    <svg viewBox="0 0 28 28"><path d="M3 17v-3a11 11 0 0 1 22 0v3h-3v-3a8 8 0 0 0-16 0v3z"/><rect x="2" y="16" width="6" height="9" rx="2"/><rect x="20" y="16" width="6" height="9" rx="2"/></svg>
    <h3>SUPPORT</h3>
    <p>Phasellus nisl est, condimentum vitae faucibus in, sollicitudin vel metus. Nunc sit amet consequat risus. Curabitur ac elit leo.</p>
    <a class="btn-dark">CONTACT US</a>
  </article>
</section>

<section class="testimonials">
  <h2 class="section-title">Testimonials</h2>
  <p class="quote"><b>&ldquo;</b> Aliquam erat volutpat. Quisque aliquet ex nec est vestibulum pulvinar. Pellentesque convallis molestie enim sit amet effici tur. Etiam id imperdiet lectus. Vivamus lacus justo, ultrices nec erat in, euismod iaculis mauris. Vivamus eleifend vitae nulla vel malesuada. In ac malesuada lacus, et consectetur ante. <b>&rdquo;</b></p>
  <p class="cite">Mara Tolley, City</p>
  <div class="dots"><i></i><i></i><i></i><i></i></div>
</section>

<section class="wrap partners" aria-label="Partner brands">
  <span>PELLING</span><span>Arvane</span><span>TESSMOOR</span><span>QUORRA</span><span>lindqvale</span><span>NORROW</span><span>HALDENE</span>
</section>

<footer class="footer">
  <div class="tagline">Praesent elementum nulla sit amet justo pellentesque scelerisque</div>
  <div class="cols">
    <div class="col"><h4>Quick Links</h4><ul><li>Home</li><li>Services</li><li>Products</li><li>Support</li><li>Contact Us</li></ul></div>
    <div class="col"><h4>My Account</h4><ul><li>Cart</li><li>Register</li><li>Login</li></ul></div>
    <div class="col"><h4>Support</h4><ul><li>FAQ</li><li>Terms of Use</li></ul></div>
    <div class="col"><h4>More Links</h4><ul><li>Aliquam erat</li><li>Quisque aliquet</li><li>Vestibulum</li><li>Curabitur ac</li><li>Aenean sed</li></ul></div>
    <div class="col wide">
      <h4>Donec vestibulum odio sem, ac laoreet massa ullamcorper id</h4>
      <p>Donec molestie nisi et tellus hendrerit vehicula. Nunc eu ligula sed quam pulvinar maximus in vitae eros. Proin porta fermentum ipsum.</p>
      <div class="social"><i></i><i></i><i></i><i></i><i></i><i></i></div>
    </div>
  </div>
</footer>
<div class="base">Copyright &copy; 2018 Brindle Fixing and Tending. All rights reserved.</div>

</body>
</html>
```